Poster Design to promote Adult Group Guitar Classes for Music School

We're a young music school trying to promote our Grown-Up Strum Starter Series classes, and need an eye catching poster design to promote the course. We'll be wanting to put the posters up on telegraph poles, community notice boards, shop front windows, cafes, shops and the around the general area of Sydney's Inner West, plus be able to covert it as a jpg image which we can forward to our mailing list and post on our website.

The poster should be visually appealing and incorporate images of what we are trying to promote.

We'd like the design to be professional, fun, creative and compliment our current logo design and colours.

Be sure to highlight 'Register Now'

Text to be used as follows:

STRUM STARTER SERIES CLASSES
For Beginner Adults

NEWTOWN

8 week Jam Packed Course
Small Groups (max. 6 people)
Guitars provided on site
Weekly hour long classes
Perfect introduction to learning the fundamentals
Materials Included
No music experience required

RESGISTER NOW – Limited Spaces
Visit our website for class times and start dates
www.brightreedmusic.com.au

T: (02) 7413 2958
E: info@brightreedmusic.com.au

PRIVATE MUSIC TUITION | ENSEMBLE | GROUP | GLEE CLUB

Industry/Entity Type

School

Requirements
Must have
• Bright Reed Music Logo

A3 poster size

Be in a print ready file for off-set printing. CMYK with 3mm bleed

```html
<!DOCTYPE html>
<html lang="en">
<head>
<meta charset="utf-8">
<title>Strum Starter Series Classes – Bright Reed Music</title>
<link rel="stylesheet" href="https://fonts.googleapis.com/css2?family=Roboto+Slab:wght@400;600;700;800&display=swap">
<style>
  :root {
    --page-bg: #ffffff;
    --ink-dark: #1a1412;
    --brand-orange: #ee6a24;
    --brand-red: #d8262b;
    --brand-gold: #f2a51d;
    --brand-teal: #5bb6c4;
    --panel-white: rgba(255, 255, 255, 0.86);
    --cream: #fdf1d6;
    --cream-deep: #f9dfa6;
    --footer-bg: #fff8e8;
    --text-muted: #3a2f28;
  }
  * { box-sizing: border-box; margin: 0; padding: 0; }
  html, body { width: 1200px; height: 900px; overflow: hidden; background: var(--page-bg); }
  body { position: relative; font-family: "Roboto Slab", Georgia, serif; }

  .poster {
    position: absolute; left: 300px; top: 22px;
    width: 603px; height: 856px;
    border: 1px solid #222;
    overflow: hidden;
    background: var(--cream);
  }

  .hero-photo {
    position: absolute; left: 0; top: 0; width: 100%; height: 603px;
    background:
      radial-gradient(ellipse at 78% 28%, #2f8fc0 0%, rgba(47,143,192,0) 28%),
      radial-gradient(ellipse at 30% 72%, #c4561c 0%, rgba(196,86,28,0) 35%),
      radial-gradient(ellipse at 55% 12%, #b37434 0%, rgba(179,116,52,0) 30%),
      radial-gradient(ellipse at 85% 75%, #e9e4dc 0%, rgba(233,228,220,0) 18%),
      linear-gradient(160deg, #2a1a10 0%, #140d09 50%, #231510 100%);
  }

  .title-panel {
    position: absolute; left: 52px; top: 0; width: 210px; height: 322px;
    background: var(--panel-white);
    text-align: center;
    padding-top: 16px;
  }
  .title-line {
    display: block;
    color: var(--brand-orange);
    font-weight: 800;
    line-height: 1;
    letter-spacing: 0.5px;
  }
  .title-line--sm { font-size: 40px; margin-bottom: 8px; }
  .title-line--xl {
    font-size: 54px; letter-spacing: -1px;
    transform: scaleY(1.75); transform-origin: center top;
    margin: 6px 0 52px;
  }
  .audience {
    margin-top: 8px;
    font-size: 17px; font-weight: 700; color: var(--ink-dark); line-height: 1.2;
  }
  .location {
    font-size: 13px; font-weight: 800; color: var(--ink-dark); letter-spacing: 0.5px;
  }

  .register-button {
    position: absolute; left: 42px; top: 330px; width: 240px; height: 45px;
    background: linear-gradient(#f9bb3a, var(--brand-gold));
    border: 2px solid #fbe3a4;
    border-radius: 3px;
    text-align: center;
    color: #fff;
  }
  .register-button__label { display: block; font-size: 20px; font-weight: 800; line-height: 1.2; padding-top: 4px; letter-spacing: 0.3px; }
  .register-button__note { display: block; font-size: 9px; font-weight: 600; line-height: 1; }

  .info-band {
    position: absolute; left: 0; top: 603px; width: 100%; height: 218px;
    background: linear-gradient(90deg, var(--cream-deep) 0%, var(--cream) 40%, var(--cream) 100%);
  }
  .brand-swirl {
    position: absolute; left: 0; top: 0; width: 260px; height: 218px;
    background: radial-gradient(ellipse at 40% 30%, rgba(246,178,76,0.45) 0%, rgba(246,178,76,0) 65%);
  }
  .brand-lockup {
    position: absolute; left: 44px; top: 48px; width: 200px; text-align: center;
  }
  .brand-mark {
    width: 66px; height: 66px; border-radius: 50%;
    background: var(--brand-orange);
    margin: 0 auto 14px;
  }
  .brand-name {
    font-size: 22px; font-weight: 700; color: var(--brand-teal); line-height: 1.1;
  }

  .feature-list {
    position: absolute; left: 290px; top: 18px; list-style: none;
    font-weight: 700; line-height: 1.15;
  }
  .feature { font-size: 22px; }
  .feature--red { color: var(--brand-red); }
  .feature--gold { color: var(--brand-gold); }
  .feature--small { font-size: 13px; line-height: 1.3; }
  .feature--large { font-size: 33px; margin-top: 2px; }

  .footer {
    position: absolute; left: 0; top: 821px; width: 100%; height: 35px;
    background: var(--footer-bg);
    text-align: center;
    color: var(--text-muted);
    padding-top: 5px;
  }
  .footer__contact { font-size: 8.5px; font-weight: 600; line-height: 1.4; }
  .footer__services { font-size: 9px; font-weight: 800; letter-spacing: 0.4px; line-height: 1.4; }
</style>
</head>
<body>
  <main class="poster">
    <div class="hero-photo" role="img" aria-label="Photograph of a pile of electric and acoustic guitars in sunburst, blue, white and natural wood finishes"></div>

    <header class="title-panel">
      <h1>
        <span class="title-line title-line--sm">STRUM</span>
        <span class="title-line title-line--sm">STARTER</span>
        <span class="title-line title-line--xl">SERIES</span>
        <span class="title-line title-line--sm">CLASSES</span>
      </h1>
      <p class="audience">For Beginner Adults</p>
      <p class="location">NEWTOWN</p>
    </header>

    <div class="register-button">
      <span class="register-button__label">RESGISTER NOW</span>
      <span class="register-button__note">Limited Spaces</span>
    </div>

    <section class="info-band">
      <div class="brand-swirl" role="img" aria-label="Soft orange swirl decoration"></div>
      <div class="brand-lockup">
        <div class="brand-mark"></div>
        <p class="brand-name">Bright Reed Music</p>
      </div>

      <ul class="feature-list">
        <li class="feature feature--red">8 week Jam Packed Course</li>
        <li class="feature feature--red">Small Groups (max. 6 people)</li>
        <li class="feature feature--gold">Guitars provided on site</li>
        <li class="feature feature--red">No music experience required</li>
        <li class="feature feature--red feature--small">Perfect introduction to learning the fundamentals</li>
        <li class="feature feature--gold">Weekly hour long classes</li>
        <li class="feature feature--red feature--large">Materials Included</li>
      </ul>
    </section>

    <footer class="footer">
      <p class="footer__contact">Visit our website for class times and start dates: www.brightreedmusic.com.au; T: (02) 7413 2958; E: info@brightreedmusic.com.au</p>
      <p class="footer__services">PRIVATE MUSIC TUITION | ENSEMBLE | GROUP | GLEE CLUB</p>
    </footer>
  </main>
</body>
</html>
```